Upscale sophisticated brochure for frameless shower doors, glass and related products for a glass c

We are a small family owned glass company working in the upscale area of lower Fairfield County Connectict .We are in need of a trifold brochure with a upscale / sophisticated theme. The name of our comany is Brightwell Pane Co. Inc.
Address- 735 West Halvern Rd. , Dunmere, Ct. 06914 phone- 203-584-7193
It should picture and have a short discription of framless shower doors. Glass table tops for bases and furniture top protection.
Mirrored walls for exersize, yoga and workout areas, bathrooms, dressing areas
Painted glass for backsplashes.pattered glass cabinet doors.
Producs and services are listed in order of importance.
The only mention of pricing is "we are competitive in our pricing".
We do have a showroom
We have been in business since 1979. That's 37 years !!
It would also need a page or area listing all other services we offer .
We are a full service glass shop. Here are some of the
services and products we offer
Shower Doors- Frameless, Sliding ,Semi Framed, Splash Panels
Shower door repair
Mirrors- clear, colored and antique for - exersize areas, gyms, bathrooms, door mirrors, dressing areas, frames,bars and backsplashes
Glass for table tops and furniture tops
Patterned glass, Painted glass, curved china cabinet glass
Saftey glass- laminated and tempered
Plexiglass
Storm and screens repaired
Fogged insulated glass replaced
Picture frame glass, window glass , plate glass
All types of glass replacement
Fireplace and wood stove glass
Showcase glass
Holes drilled for aquariums
And much more

Target Market(s)

Homeowners / (second area contractors)

Industry/Entity Type

It Company

Font styles to use
Serif

Requirements
Must have
• Photos- more traditional , some modern, brief description under /next to some photos. One page listing other services we provide
• Brief bio of who we are- family business serving Greenwich and surrouding communities since 1978.(will elaborate more when needed)
Nice to have
• Check glass company and shower door websites for ideas
• sir rainfall panel,
• keystoneclearline shower doors westport ct.
• Verrow glass - good wording and copy
Should not have
• We do not do any commercial buildings a residential theme should be used.
• we do not do web sales
• we are not a bargain/ discount business
• do not put call now for a estimate
• pictures of product not people
• No Mailing space area. If mailed I will use a envelope.

```html
<!DOCTYPE html>
<html lang="en">
<head>
<meta charset="utf-8">
<title>Brightwell Pane Co. Inc. – Trifold Brochure</title>
<link href="https://fonts.googleapis.com/css2?family=Open+Sans:wght@400;700&display=swap" rel="stylesheet">
<style>
  :root {
    --page-bg: #ece7de;
    --paper: #ffffff;
    --brand-green: #217a12;
    --band-green: #4f8f3a;
    --frame-beige: #e6dfd0;
    --text-white: #ffffff;
  }
  html, body {
    margin: 0;
    padding: 0;
    width: 1200px;
    height: 1200px;
    overflow: hidden;
    background: var(--page-bg);
    font-family: "Open Sans", sans-serif;
  }
  .brochure {
    position: absolute;
    left: 30px;
    top: 197px;
    width: 1140px;
    height: 806px;
    background: var(--paper);
    box-shadow: 0 4px 14px rgba(0,0,0,0.18);
  }
  .panel { position: absolute; top: 0; height: 806px; width: 380px; }
  .panel--about { left: 0; }
  .panel--contact { left: 380px; }
  .panel--cover { left: 760px; }

  .framed-photo {
    position: absolute;
    left: 42px;
    width: 280px;
    height: 177px;
    border: 8px solid var(--frame-beige);
  }
  .framed-photo--vanity {
    top: 42px;
    background: linear-gradient(95deg, #eeeeea 0%, #c9c7bd 25%, #7a7468 50%, #a59d8a 70%, #ddd8cb 100%);
  }
  .framed-photo--shower {
    top: 288px;
    background: linear-gradient(95deg, #e7e8e6 0%, #f3f3f1 35%, #cdd3d6 65%, #eceeee 100%);
  }

  .about-copy {
    position: absolute;
    left: 46px;
    top: 534px;
    width: 300px;
    margin: 0;
    color: var(--brand-green);
    font-size: 15.6px;
    line-height: 16.5px;
  }
  .about-copy p { margin: 0 0 16.5px; }

  .hero-photo {
    position: absolute;
    left: 380px;
    top: 0;
    width: 760px;
    height: 510px;
    background: linear-gradient(165deg, #f0f0ec 0%, #dcdedb 22%, #9db08c 40%, #c9ccc6 55%, #8a6a4a 78%, #3a3835 100%);
  }
  .hero-band {
    position: absolute;
    left: 380px;
    top: 510px;
    width: 760px;
    height: 11px;
    background: var(--band-green);
  }
  .hero-tagline {
    position: absolute;
    left: 790px;
    top: 390px;
    width: 320px;
    margin: 0;
    text-align: center;
    color: var(--text-white);
    font-weight: 700;
    font-size: 25px;
    line-height: 34px;
    text-shadow: 0 1px 3px rgba(0,0,0,0.35);
  }

  .contact-block {
    position: absolute;
    top: 521px;
    left: 0;
    width: 380px;
    height: 285px;
    background: var(--brand-green);
    color: var(--text-white);
    text-align: center;
    font-size: 16.5px;
    line-height: 18px;
  }
  .contact-block p { margin: 0; }
  .contact-block .company-name { font-weight: 700; margin-top: 63px; }
  .contact-block .web { font-weight: 700; margin-top: 18px; }
  .contact-block .license { margin-top: 18px; }

  .cover-fold {
    position: absolute;
    top: 521px;
    left: 0;
    width: 380px;
    height: 285px;
    background: linear-gradient(90deg, #e4e4e4 0%, #ffffff 12%, #ffffff 100%);
  }
  .brand-name {
    position: absolute;
    left: 0;
    top: 642px;
    width: 380px;
    text-align: center;
    color: var(--brand-green);
    font-weight: 700;
    font-size: 27px;
    margin: 0;
  }
</style>
</head>
<body>
  <main class="brochure">
    <section class="panel panel--about">
      <div class="framed-photo framed-photo--vanity" role="img" aria-label="Bathroom vanity with large framed mirror and glass shelves"></div>
      <div class="framed-photo framed-photo--shower" role="img" aria-label="Bright bathroom with double vanity and frameless glass shower enclosure"></div>
      <div class="about-copy">
        <p>Brightwell Pane is a family owned and operated business serving Greenwich and the surrounding area since 1978. We are licensed, insured and a member of the Connecticut Glass Trades Guild.</p>
        <p>We pride ourselves in providing quality products, superior workmanship and courteous, reliable service. Our staff is friendly, knowledgeable and always willing to provide the extra assistance you may need.</p>
      </div>
    </section>

    <div class="hero-photo" role="img" aria-label="Bright kitchen with white cabinets, wood island, glass backsplash and garden windows"></div>
    <div class="hero-band"></div>
    <p class="hero-tagline">Serving Greenwich<br>and Surrounding Areas</p>

    <section class="panel panel--contact">
      <div class="contact-block">
        <p class="company-name">Brightwell Pane Co. Inc.</p>
        <p>735 West Halvern Rd.</p>
        <p>Dunmere, Connecticut 06914</p>
        <p>Phone: 203-584-7193</p>
        <p class="web">www.brightwellpane.com</p>
        <p class="license">Licensed and insured</p>
        <p>CT License # 472316</p>
      </div>
    </section>

    <section class="panel panel--cover">
      <div class="cover-fold"></div>
      <p class="brand-name">Brightwell Pane Co. Inc.</p>
    </section>
  </main>
</body>
</html>
```